Business Card Ayurvedic Massage

I'm starting with my ayurvedic massage business and need a business card design. The design should be inline with my brand/logo as well as with the design of my website (www.mirelo-dant.ch).
Front: logo and text "Ayurvedische Massagen"
back: name and adress (see details https://www.mirelo-dant.ch/kontakt.html)

```html
<!DOCTYPE html>
<html lang="de">
<head>
<meta charset="utf-8">
<title>Mirelo-Dant – Visitenkarte</title>
<link rel="stylesheet" href="https://fonts.googleapis.com/css2?family=EB+Garamond:wght@400;500&display=swap">
<style>
  :root {
    --page-bg: #e9e4dc;
    --card-red: #7e0010;
    --card-red-deep: #6a000c;
    --card-cream: #f3e6d2;
    --gold: #d9a640;
    --gold-light: #f0c865;
    --ink-red: #6e1418;
    --elephant-plum: #8a4a52;
  }
  * { margin: 0; padding: 0; box-sizing: border-box; }
  html, body { width: 1200px; height: 900px; overflow: hidden; }
  body {
    background: var(--page-bg);
    font-family: "EB Garamond", Georgia, serif;
    display: flex;
    flex-direction: column;
    align-items: center;
    justify-content: center;
    gap: 36px;
  }
  .card {
    width: 680px;
    height: 396px;
    position: relative;
    box-shadow: 0 6px 18px rgba(0,0,0,0.18);
  }
  /* Front */
  .card--front {
    background: radial-gradient(ellipse at center, var(--card-red) 0%, var(--card-red-deep) 100%);
  }
  .front-pattern {
    position: absolute; inset: 0;
  }
  .front-logo-row {
    position: absolute;
    left: 0; right: 0; top: 108px;
    display: flex;
    align-items: center;
    justify-content: center;
    gap: 22px;
  }
  .elephant {
    width: 120px;
    height: 118px;
    border-radius: 10px;
    background: linear-gradient(150deg, var(--gold-light) 0%, var(--gold) 45%, var(--elephant-plum) 100%);
  }
  .brand-name {
    font-family: "EB Garamond", Georgia, serif;
    font-weight: 500;
    font-size: 44px;
    color: var(--gold);
    letter-spacing: 1px;
    line-height: 1;
  }
  .tagline {
    position: absolute;
    left: 0; right: 0; top: 272px;
    text-align: center;
    font-size: 25px;
    letter-spacing: 1.5px;
    color: var(--gold-light);
  }
  /* Back */
  .card--back { background: var(--card-cream); }
  .back-logo-row {
    position: absolute;
    left: 28px; right: 28px; top: 34px;
    display: flex;
    align-items: center;
    justify-content: space-between;
  }
  .back-logo-row .elephant { width: 150px; height: 140px; opacity: 0.85; }
  .back-logo-row .brand-name { font-size: 48px; color: var(--gold); }
  .contact {
    position: absolute;
    left: 44px; bottom: 34px; right: 44px;
    display: flex;
    justify-content: space-between;
    align-items: flex-end;
    color: var(--ink-red);
    font-size: 17px;
    line-height: 1.35;
  }
  .contact-lines { list-style: none; }
  .contact-address { text-align: right; }
</style>
</head>
<body>

  <section class="card card--front" aria-label="Vorderseite">
    <div class="front-pattern" role="img" aria-label="Dezentes rotes Damastmuster im Hintergrund"></div>
    <div class="front-logo-row">
      <div class="elephant" role="img" aria-label="Goldene Illustration eines geschmückten Elefanten mit Schirm"></div>
      <span class="brand-name">mirelo-dant</span>
      <div class="elephant" role="img" aria-label="Goldene Illustration eines geschmückten Elefanten mit Schirm"></div>
    </div>
    <p class="tagline">AYURVEDISCHE MASSAGEN</p>
  </section>

  <section class="card card--back" aria-label="Rückseite">
    <div class="back-logo-row">
      <div class="elephant" role="img" aria-label="Illustration eines geschmückten Elefanten in Gold und Altrosa"></div>
      <span class="brand-name">mirelo-dant</span>
      <div class="elephant" role="img" aria-label="Illustration eines geschmückten Elefanten in Gold und Altrosa"></div>
    </div>
    <div class="contact">
      <ul class="contact-lines">
        <li>+41 77 380 24 61 (Bitte keine SMS)</li>
        <li>www.mirelo-dant.ch</li>
        <li>info@mirelo-dant.ch</li>
        <li>Lena Vorbach, mirelo-dant</li>
      </ul>
      <p class="contact-address">Mühlegasse 7<br>8836 Bennenburg (SZ)</p>
    </div>
  </section>

</body>
</html>
```